依頼概要
■依頼の概要
婚活男子に向けた電子書籍(pagelo出版)の表紙デザイン作成をお願いします。
電子書籍なので、タイトルがはっきり分かるものでお願いします。

■本の内容
婚活中の男性が、婚活成幸するための方法や事例を書いています。
婚活男子に、勇気・元気・やる気と知識を与える内容となっています。
原稿内容を添付します。

■読者ターゲット
文字通り、婚活がうまくいかない男性全般
(・無口でおしゃべりが続かない・女性のことがサッパリ分からない・いい加減、婚活を卒業したい・草食系男子etc…と言ったところでしょうか)

■デザイン要望
原稿内容を参考にしていただいて、より売れることを目的としたデザインにしてください。
デザイナーさんのパフォーマンスを引き出したいので、デザイナーさんのセンスにお任せします。
また、下記の内容にもご注意ください。

■お願い&ご相談
今回は男性版ですが、同じシリーズで女性版も(できれば2ヶ月以内に)出したいと思っています。
それでできれば、「色違い」「類似デザイン」(多少の文字変更有り)で、同シリーズとして認知してもらえるような、デザインを希望しています。
尚、女性版の際に文字やデザインを修正していただく場合、対応可能かと、その場合の追加料金についても合わせてお知らせください。

■その他
Tasqoraの利用含め初めての経験で私自身分からないことばかりですが、何かご不明な点がございましたら、お気軽にご質問ください。
■タイトル&サブキャッチ
タイトル:縁探しに迷っている男子に贈る一冊
サブキャッチ:~会話・外見・条件に自信がなくても結婚できる~

■著者
婚活成幸シフトナビゲーター 柊 あき(ひいらぎ あき)
肩書(婚活成幸シフトナビゲーター)と読み仮名を入れる・入れないはデザイナーさんの感性にお任せします。
尚、読み仮名を入れる場合、上記のように()書きにするか、紡の上にルビを振るかも含めてお任せします。
■読者プレゼント
『惹かれる人』に変わる魔法の言い回し
ご提案をいただけて、さすがプロのデザイナーさんはセンスが違うな~と感心しております(*^-^*)
まだまだいろんな切り口のデザインを考えていただき、ご提案いただけましたら有難く嬉しく思います。
また私はデザインの素人で何も分かりませんが、デザインだけでなく添付ファイル原稿(1時間で読めます)の中から読者に響く文言を拾っていただいて入れていただいても嬉しく思います。

Tasqora 初めての利用で分からないことばかりですが、デザイナーさんはデザインだけでなくご対応にもプロ意識がみえてとても嬉しく思っております(^o^)
引き続きご提案を募集させていただきますので、皆様ご提案の程どうぞ宜しくお願い申し上げますm(__)m
最初に予定していた日にちには他の準備が間に合わなくなりましたので、せっかくなので締切日を1日延ばしました。
引き続きステキなご提案をいただけましたら嬉しい限りです。
デザイナーの皆様、何卒よろしくお願い致しますm(__)m
デザイナーの皆様、たくさんご提案をいただきまして本当にありがとうございます。
お一人お一人にお礼の言葉をお贈りしたいのですが、今日は締切日だからかいつもになくたくさんご提案をいただいて、コメントが間に合いません。
ですので、ここでまとめてお礼の言葉をお贈りさせていただきたいと思います。
どれもプロの皆様のお仕事はステキなものばかりで、ここ何日もどれにしようか・・・悩み続けておりました。
正直、私一人では決めかねてますので、他の方のご意見も伺ってから決めさせていただこうと考えております。
IT超苦手でTasqora初めての利用の私です。
正直まだ利用方法すら理解していない状況ですが、皆様のお気持ちが有難くって有難くって、もう本当に感謝しかありません。
本当にほんとうにありがとうございますm(__)m
しかし、利用方法をあまり理解しておりませんので、今までに失礼なことがあったようでしたら謝らせていただきます。申し訳ございませんm(__)m
この度は、皆様本当にありがとうございました!

20名弱ほどの方々に表紙デザイン選挙・投票をいただいて決めさせていただきました。
その結果、ぶっちぎりの断トツ1位であったため決めさせていただきました。
こちらのデザイナー様は、私の原稿をよくお読みいただいているな~と感じました。
その意を汲んでいただいたものが表紙に表れていると思います。
事前にお知らせしたタイトルや名前・読者プレゼント以外にも原稿を読んでいただいたからこそ分かるキャッチ―な文言を取り入れてくださり、それにあったデザインに仕上がっていると思っております。

この度は、皆様からたくさんのご提案をいただきありがとうございました。
ステキなご提案をたくさんいただけて私一人では決められずにおりましたので、まず、スピリチュアルの方に一つずつ見ていただき1つ1つ解説をいただきました。
そのうえである程度「良し」とされたものの中から、20人弱の方々に投票を行っていただいて決めさせていただきました。
本来ならお一人お一人にお礼の言葉をお贈りさせていただかなければならないのだと思いますが、この場を借りて心から感謝&お礼を申し上げます。
本当にありがとうございました。

```html
<!DOCTYPE html>
<html lang="ja">
<head>
<meta charset="utf-8">
<title>縁探しに迷っている男子に贈る一冊</title>
<link rel="stylesheet" href="https://fonts.googleapis.com/css2?family=Noto+Sans+JP:wght@500;700;900&display=swap">
<style>
  :root {
    --magenta: #e3157f;
    --ink: #141414;
    --white: #ffffff;
    --photo-light: #e9e4e6;
    --photo-mid: #b9aeb4;
    --photo-dark: #6f6469;
    --skin: #d9b3a8;
  }
  * { margin: 0; padding: 0; box-sizing: border-box; }
  html, body { width: 750px; height: 1200px; overflow: hidden; background: var(--white); }
  .cover {
    position: relative;
    width: 750px; height: 1200px;
    overflow: hidden;
    font-family: "Noto Sans JP", sans-serif;
  }
  .cover-photo {
    position: absolute; inset: 0;
    background:
      radial-gradient(ellipse 55% 40% at 45% 55%, var(--skin) 0%, rgba(217,179,168,0) 70%),
      linear-gradient(160deg, var(--photo-light) 0%, var(--photo-mid) 45%, var(--photo-dark) 100%);
  }
  .outlined {
    paint-order: stroke fill;
    -webkit-text-stroke: 10px var(--white);
  }
  .catch {
    position: absolute; top: 30px; left: 0; width: 750px;
    text-align: center;
    color: var(--magenta);
    font-weight: 900;
    font-size: 56px;
    line-height: 1.25;
  }
  .title-vertical {
    position: absolute; top: 215px; right: 28px;
    writing-mode: vertical-rl;
    font-size: 100px; font-weight: 900;
    color: var(--ink);
    line-height: 1;
  }
  .title-line {
    position: absolute;
    font-weight: 900; color: var(--ink);
    line-height: 1;
    white-space: nowrap;
  }
  .title-line--second { top: 620px; left: 36px; font-size: 104px; }
  .title-line--key { top: 842px; left: 50px; font-size: 160px; color: var(--magenta); }
  .title-line--last { top: 1030px; left: 170px; font-size: 82px; }
  .author {
    position: absolute; top: 762px; right: 36px;
    text-align: right; color: var(--white);
    font-weight: 700;
    text-shadow: 0 0 6px rgba(0,0,0,0.5);
  }
  .author-role { font-size: 19px; }
  .author-name { font-size: 32px; letter-spacing: 0.1em; }
  .present {
    position: absolute; left: 408px; top: 830px; width: 330px;
    text-align: center;
  }
  .present-label {
    display: inline-block;
    background: var(--white);
    color: var(--magenta);
    font-weight: 900; font-size: 30px;
    padding: 4px 18px;
    margin-bottom: 14px;
  }
  .present-gift {
    background: rgba(255,255,255,0.85);
    color: var(--magenta);
    font-weight: 900; font-size: 27px;
    line-height: 1.4;
    padding: 12px 6px;
    white-space: nowrap;
  }
</style>
</head>
<body>
<main class="cover">
  <div class="cover-photo" role="img" aria-label="白いキャミソールの人物が小さな白い野花の束を手に持ち、淡く柔らかな光の中に立つ写真"></div>

  <p class="catch outlined">会話・外見・条件に<br>自信がなくても結婚できる。</p>

  <h1 class="book-title">
    <span class="title-vertical outlined">縁探しに</span>
    <span class="title-line title-line--second outlined">迷っている</span>
    <span class="title-line title-line--key outlined">男子</span>
    <span class="title-line title-line--last outlined">に贈る一冊</span>
  </h1>

  <div class="author">
    <p class="author-role">婚活成幸シフトナビゲーター</p>
    <p class="author-name">柊 あき</p>
  </div>

  <div class="present">
    <p class="present-label">読者プレゼント</p>
    <p class="present-gift">『惹かれる人』に変わる<br>魔法の言い回し</p>
  </div>
</main>
</body>
</html>
```